Young Architect Bussiness Card

English is not my first language (spanish is).
Need a bussiness card design for my best friend who is about to graduate from college, Licentiate degree in architecture, so she needs business cards to start networking, currently she has no porfolio, web page or facebook. so she is relying on her cel phone and gmail, but should leave space for one of them (facebook)

Design for business card should be modern, maybe something with construction blue prints patern or 3D modelling.

Name: Mariela Ocampo Valverde
Licentiate in Arquitecture
Cel: (506) XXX-8270
email: marielaXXX@correonube.net

Services, although im not sure if it has to be there or not:
Anteproyectos / Proposal design
Inspecciones / Site Inspections
Modelado 3D / 3D modelling
Planos Constructivos / Construction Blue Prints
Presupuestos / Budgets

Design should be in spanish

Industry/Entity Type

Architect

Contact Information for Business Card

Name: Mariela Ocampo, Arquitecto
Associtation code : XXXX
Phone: (506) XXXX-XXXX
Email: xxx@correonube.net
Facebook: xxxx

Requirements
Must have
• Design for business card should be modern, maybe something with construction blue prints patern or 3D modelling.
Nice to have
• Something like a transition from 2D to 3D.

```html
<!DOCTYPE html>
<html lang="es">
<head>
<meta charset="utf-8">
<title>Tarjeta de presentación — Mariela Ocampo Valverde</title>
<link rel="stylesheet" href="https://fonts.googleapis.com/css2?family=Mulish:wght@400;700&display=swap">
<style>
  :root {
    --page-bg: #eef0f3;
    --card-bg: #ffffff;
    --ink-navy: #1d4f80;
    --ink-blue: #245d8f;
    --ink-grey: #3a3a3a;
    --band-light: #e9eef4;
    --band-mid: #b9c6d6;
    --band-dark: #7f95b3;
    --line-blue: #5d7ea6;
    --art-light: #f4f6f9;
    --art-mid: #d5dce6;
  }
  * { margin: 0; padding: 0; box-sizing: border-box; }
  html, body {
    width: 1107px; height: 1200px; overflow: hidden;
    background: var(--page-bg);
    font-family: "Mulish", "Century Gothic", sans-serif;
  }
  .canvas { position: relative; width: 1107px; height: 1200px; }
  .card {
    position: absolute; left: 143px; width: 820px; height: 464px;
    background: var(--card-bg); overflow: hidden;
    box-shadow: 0 3px 10px rgba(0,0,0,.18);
  }
  .card--front { top: 96px; }
  .card--back { top: 628px; }
  .card__decor { position: absolute; inset: 0; width: 820px; height: 464px; }
  .card__art {
    position: absolute; border-radius: 50% 50% 46% 46%;
    background: radial-gradient(ellipse at 50% 50%, var(--art-mid) 0%, var(--art-light) 55%, rgba(255,255,255,0) 75%);
  }
  .card--front .card__art { left: 2px; top: 112px; width: 400px; height: 326px; }
  .card--back .card__art { left: 392px; top: 108px; width: 410px; height: 310px; }

  .identity { position: absolute; right: 59px; top: 0; text-align: right; }
  .identity__name {
    position: absolute; right: 0; top: 106px; white-space: nowrap;
    font-weight: 700; font-size: 26px; color: var(--ink-navy);
  }
  .identity__line {
    position: absolute; right: 0; white-space: nowrap;
    font-size: 20.5px; color: var(--ink-grey);
  }
  .identity__degree { top: 152px; }
  .identity__code { top: 190px; }

  .contact { position: absolute; right: 53px; white-space: nowrap;
    font-size: 20.5px; color: var(--ink-grey);
    display: flex; align-items: center; gap: 12px; }
  .contact--phone { top: 256px; }
  .contact--mail { top: 293px; }
  .contact--social { top: 330px; }
  .contact__icon { width: 22px; height: 22px; flex: none; }

  .services { position: absolute; left: 88px; top: 122px; list-style: none; }
  .services__item {
    font-size: 22px; line-height: 39.5px; color: var(--ink-blue); white-space: nowrap;
  }
  .services__item::before { content: "•"; margin-right: 8px; font-size: 16px; vertical-align: 2px; }
</style>
</head>
<body>
<main class="canvas">

  <section class="card card--front">
    <svg class="card__decor" viewBox="0 0 820 464" aria-hidden="true">
      <defs>
        <linearGradient id="front-band" x1="0" x2="1" y1="0" y2="0">
          <stop offset="0" stop-color="var(--band-mid)"/>
          <stop offset=".4" stop-color="var(--band-light)"/>
          <stop offset="1" stop-color="var(--band-dark)"/>
        </linearGradient>
      </defs>
      <path d="M0 0 H820 V58 Q420 36 160 110 Q50 145 0 205 Z" fill="url(#front-band)"/>
      <path d="M0 205 Q50 145 160 110 Q420 36 820 58" fill="none" stroke="var(--line-blue)" stroke-width="3"/>
      <path d="M0 232 Q70 150 240 112 Q480 62 820 70" fill="none" stroke="var(--band-mid)" stroke-width="2"/>
      <path d="M560 464 Q720 440 800 340" fill="none" stroke="var(--band-mid)" stroke-width="7"/>
      <path d="M600 464 Q740 445 812 360" fill="none" stroke="var(--line-blue)" stroke-width="2"/>
    </svg>
    <div class="card__art" role="img" aria-label="Ilustración de un complejo de edificios en modelo 3D sobre planos, con un lápiz"></div>

    <div class="identity">
      <h1 class="identity__name">Mariela Ocampo Valverde</h1>
      <p class="identity__line identity__degree">Licentiate in Arquitecture</p>
      <p class="identity__line identity__code">Associtation code: XXXX</p>
    </div>

    <p class="contact contact--phone">(506) XXX-8270
      <svg class="contact__icon" viewBox="0 0 22 22" aria-hidden="true"><rect x="5" y="1.5" width="12" height="19" rx="1.5" fill="none" stroke="var(--ink-navy)" stroke-width="2"/><line x1="9" y1="17.5" x2="13" y2="17.5" stroke="var(--ink-navy)" stroke-width="1.5"/></svg>
    </p>
    <p class="contact contact--mail">marielaXXX@correonube.net
      <svg class="contact__icon" viewBox="0 0 22 22" aria-hidden="true"><rect x="2" y="5" width="18" height="12" fill="var(--ink-navy)"/><path d="M2 5 L11 12 L20 5" fill="none" stroke="#fff" stroke-width="1.6"/></svg>
    </p>
    <p class="contact contact--social">mariela XXX
      <svg class="contact__icon" viewBox="0 0 22 22" aria-hidden="true"><rect x="2" y="2" width="18" height="18" fill="var(--ink-navy)"/></svg>
    </p>
  </section>

  <section class="card card--back">
    <svg class="card__decor" viewBox="0 0 820 464" aria-hidden="true">
      <defs>
        <linearGradient id="back-band" x1="0" x2="1" y1="0" y2="0">
          <stop offset="0" stop-color="var(--band-dark)"/>
          <stop offset=".5" stop-color="var(--band-light)"/>
          <stop offset="1" stop-color="var(--band-mid)"/>
        </linearGradient>
      </defs>
      <path d="M0 0 H820 V92 Q560 28 260 36 Q90 42 0 72 Z" fill="url(#back-band)"/>
      <path d="M0 72 Q90 42 260 36 Q560 28 820 92" fill="none" stroke="var(--line-blue)" stroke-width="3"/>
      <path d="M0 84 Q140 50 360 50 Q620 55 820 120" fill="none" stroke="var(--band-mid)" stroke-width="2"/>
      <path d="M0 340 Q60 420 250 464" fill="none" stroke="var(--band-mid)" stroke-width="7"/>
      <path d="M0 372 Q70 440 200 464" fill="none" stroke="var(--line-blue)" stroke-width="2"/>
    </svg>
    <div class="card__art" role="img" aria-label="Ilustración de un complejo de edificios en modelo 3D sobre planos, con un lápiz"></div>

    <ul class="services">
      <li class="services__item">Anteproyectos</li>
      <li class="services__item">Inspecciones</li>
      <li class="services__item">Modelado 3D</li>
      <li class="services__item">Planos Constructivos</li>
      <li class="services__item">Presupuestos</li>
    </ul>
  </section>

</main>
</body>
</html>
```